New Webpage for High Class Expert Witness Services Company

We are looking for a minimalist design for a webpage that just has our logo and an entry form offer to connect with one of our Liaisons.
The entry form should just ask for Name, Email, Contact Info and Description of Project.

Company Name is: The Marlowe Crest Defense Services

Number of Pages Required

1 page

```html
<!DOCTYPE html>
<html lang="en">
<head>
<meta charset="utf-8">
<title>Marlowe Crest Defense Services — Connect with a Liaison</title>
<link rel="stylesheet" href="https://fonts.googleapis.com/css2?family=Cinzel:wght@400;700&family=Roboto:wght@400&display=swap">
<style>
  :root {
    --bg-deep: #1f1f1f;
    --bg-mid: #2b2b2b;
    --bg-glow: #3a3a3a;
    --eyebrow: #6c6c6c;
    --headline-top: #bdbdbd;
    --headline-bottom: #8e8e8e;
    --panel-border: #5c5c5c;
    --field-border: #8a8a8a;
    --text-light: #f2f2f2;
    --button-light: #e4e4e4;
    --button-dark: #858585;
    --button-text: #111111;
  }
  * { box-sizing: border-box; margin: 0; padding: 0; }
  html, body { width: 1200px; height: 741px; overflow: hidden; background: var(--bg-deep); }
  .page {
    position: relative;
    width: 1200px;
    height: 741px;
    overflow: hidden;
    background:
      radial-gradient(ellipse 420px 300px at 420px 170px, var(--bg-glow), transparent 70%),
      radial-gradient(ellipse 700px 500px at 900px 300px, #303030, transparent 75%),
      linear-gradient(160deg, var(--bg-mid), var(--bg-deep));
  }
  .crest-backdrop {
    position: absolute;
    left: 347px;
    top: 93px;
    width: 360px;
    height: 494px;
    background: radial-gradient(ellipse 200px 160px at 90px 80px, rgba(90,90,90,0.35), rgba(30,30,30,0.15) 70%, transparent);
    opacity: 0.9;
  }
  .hero { position: absolute; left: 136px; top: 268px; }
  .hero-eyebrow {
    font-family: "Cinzel", serif;
    font-size: 18.5px;
    letter-spacing: 2.2px;
    color: var(--eyebrow);
    margin-left: 3px;
  }
  .hero-title {
    font-family: "Cinzel", serif;
    font-weight: 400;
    font-size: 52px;
    line-height: 58px;
    letter-spacing: 1.5px;
    margin-top: 6px;
    background: linear-gradient(180deg, var(--headline-top), var(--headline-bottom));
    -webkit-background-clip: text;
    background-clip: text;
    color: transparent;
  }
  .liaison-form {
    position: absolute;
    left: 716px;
    top: 124px;
    width: 378px;
    height: 437px;
    border: 1px solid var(--panel-border);
    background:
      radial-gradient(ellipse 200px 130px at 330px 380px, rgba(85,85,85,0.5), transparent 70%),
      linear-gradient(160deg, #2a2a2a, #1c1c1c);
    padding: 36px 0 0 44px;
  }
  .form-title {
    font-family: "Cinzel", serif;
    font-weight: 400;
    font-size: 21px;
    letter-spacing: 0.4px;
    color: var(--text-light);
    margin-bottom: 24px;
    white-space: nowrap;
  }
  .form-field {
    display: block;
    width: 293px;
    height: 42px;
    margin-bottom: 12px;
    border: 1px solid var(--field-border);
    background: transparent;
    padding: 0 17px;
    font-family: "Roboto", sans-serif;
    font-size: 13px;
    color: var(--text-light);
    outline: none;
  }
  .form-field::placeholder { color: var(--text-light); opacity: 1; }
  .form-field--message {
    height: 88px;
    padding-top: 11px;
    resize: none;
    margin-bottom: 13px;
  }
  .submit-button {
    display: block;
    width: 297px;
    height: 44px;
    border: none;
    background: linear-gradient(90deg, var(--button-light), var(--button-dark));
    font-family: "Cinzel", serif;
    font-weight: 700;
    font-size: 15px;
    letter-spacing: 0.5px;
    color: var(--button-text);
    cursor: pointer;
  }
  .footer-tagline {
    position: absolute;
    left: 0;
    right: 0;
    top: 678px;
    text-align: center;
    font-family: "Cinzel", serif;
    font-size: 16.5px;
    color: var(--text-light);
    letter-spacing: 0.2px;
    padding-left: 14px;
  }
  .footer-rule {
    position: absolute;
    left: 54px;
    top: 730px;
    width: 152px;
    height: 2px;
    background: #2c2c2c;
  }
</style>
</head>
<body>
<main class="page">
  <div class="crest-backdrop" role="img" aria-label="Large faint embossed emblem of The Marlowe Crest Defense Services"></div>

  <section class="hero">
    <p class="hero-eyebrow">MARLOWE CREST DEFENSE SERVICES</p>
    <h1 class="hero-title">SEAMLESS<br>MEDICAL EXPERT<br>INTEGRATION</h1>
  </section>

  <form class="liaison-form">
    <h2 class="form-title">CONNECT WITH A LIAISON</h2>
    <input class="form-field" type="text" placeholder="Name*" aria-label="Name">
    <input class="form-field" type="email" placeholder="Email*" aria-label="Email">
    <input class="form-field" type="tel" placeholder="Phone number*" aria-label="Phone number">
    <textarea class="form-field form-field--message" placeholder="Description of Services Needed" aria-label="Description of Services Needed"></textarea>
    <button class="submit-button" type="submit">SUBMIT</button>
  </form>

  <p class="footer-tagline">SEAMLESS MEDICAL EXPERT INTEGRATION</p>
  <div class="footer-rule"></div>
</main>
</body>
</html>
```